Water ATM Card

Need a design for water ATM cards. Size of card is 3.375 x 2.125 inch
On the Front include the Cedar brook Logo.
Bottom right corner should have Price $100
On the Back
This card is to be used to access water refills at any Cedar Brook Water Vending Machines.
Please contact (869) 614 2938 or (869) 731 4072 or email clearflowhq@examplemail.com for any assistance or recharging of card.

```html
<!DOCTYPE html>
<html lang="en">
<head>
<meta charset="utf-8">
<title>Cedar Brook Water ATM Card</title>
<link href="https://fonts.googleapis.com/css2?family=Montserrat:wght@500;700;800&family=Lexend:wght@400;500&family=Oswald:wght@500&display=swap" rel="stylesheet">
<style>
  :root {
    --stage: #939598;
    --blue: #1b75bc;
    --blue-dark: #1c5aa8;
    --navy: #27398c;
    --green: #1f9a48;
    --green-light: #7cc242;
    --brand-blue: #1a6fc0;
    --water-deep: #2f78c4;
    --water-light: #a9cdee;
    --white: #ffffff;
    --ink: #111111;
  }
  * { box-sizing: border-box; margin: 0; padding: 0; }
  html, body { width: 1115px; height: 1200px; overflow: hidden; }
  body { background: var(--stage); position: relative; font-family: "Lexend", sans-serif; }

  .side-label {
    position: absolute; left: 84px; font-family: "Lexend", sans-serif;
    font-size: 29px; color: var(--ink); line-height: 1;
  }
  .side-label--front { top: 314px; }
  .side-label--back { top: 854px; }

  .card { position: absolute; left: 247px; width: 754px; height: 474px; overflow: hidden; background: var(--white); }
  .card--front { top: 93px; }
  .card--back { top: 633px; }

  /* Front */
  .title-banner { position: absolute; left: 0; top: 0; width: 754px; height: 120px; }
  .title-word {
    position: absolute; font-family: "Montserrat", sans-serif; color: var(--white);
    font-size: 54px; line-height: 1; letter-spacing: 0.5px;
  }
  .title-word--water { left: 95px; top: 42px; font-weight: 500; }
  .title-word--atm { left: 363px; top: 42px; }
  .title-word--atm strong { font-weight: 800; }
  .title-word--atm span { font-weight: 500; }

  .brand-name {
    position: absolute; left: 0; width: 754px; top: 206px; text-align: center;
    font-family: "Montserrat", sans-serif; font-weight: 800; font-size: 33px;
    color: var(--brand-blue); letter-spacing: 1px; line-height: 1;
  }
  .brand-tagline {
    position: absolute; left: 0; width: 754px; top: 238px; text-align: center;
    font-family: "Lexend", sans-serif; font-weight: 400; font-size: 20px;
    color: var(--brand-blue); letter-spacing: 0.5px; line-height: 1;
  }

  .water-photo {
    position: absolute; left: 0; top: 270px; width: 754px; height: 190px;
    background: linear-gradient(180deg, rgba(255,255,255,0) 0%, var(--water-deep) 25%, #5d9ad6 60%, var(--water-light) 100%);
  }
  .front-wave { position: absolute; left: 0; top: 415px; width: 754px; height: 59px; }

  .price-badge {
    position: absolute; left: 614px; top: 249px; width: 108px; height: 108px;
    border-radius: 50%; background: var(--white); border: 2px solid var(--navy);
    box-shadow: 0 0 0 3px var(--white);
    text-align: center; color: var(--navy);
  }
  .price-label {
    display: block; margin-top: 20px; font-family: "Montserrat", sans-serif;
    font-weight: 800; font-size: 21px; line-height: 1; color: var(--brand-blue);
  }
  .price-value {
    display: block; font-family: "Oswald", sans-serif; font-weight: 500;
    font-size: 44px; line-height: 1;
  }

  /* Back */
  .back-top-band {
    position: absolute; left: 0; top: 0; width: 754px; height: 49px;
    background: linear-gradient(100deg, var(--green), var(--green-light));
  }
  .back-stripe { position: absolute; left: 0; top: 49px; width: 754px; height: 109px; background: var(--white); }
  .back-panel {
    position: absolute; left: 0; top: 158px; width: 754px; height: 316px;
    background: linear-gradient(110deg, var(--green), var(--green-light));
  }
  .chip {
    position: absolute; left: 50px; top: 198px; width: 100px; height: 84px;
    border-radius: 11px; background: var(--navy);
  }
  .usage-note {
    position: absolute; left: 184px; top: 211px; width: 475px;
    font-family: "Lexend", sans-serif; font-size: 14.5px; line-height: 18.5px; color: var(--white);
  }
  .back-wave { position: absolute; left: 0; top: 290px; width: 754px; height: 184px; }

  .contact-heading {
    position: absolute; left: 0; width: 754px; top: 352px; text-align: center;
    font-family: "Lexend", sans-serif; font-weight: 500; font-size: 27px; line-height: 1;
    color: var(--green-light); letter-spacing: 0.3px;
  }
  .contact-line {
    position: absolute; top: 391px; font-family: "Lexend", sans-serif; font-size: 20px;
    line-height: 1; color: var(--white); white-space: nowrap;
  }
  .contact-line--phone { left: 62px; }
  .contact-line--email { left: 434px; top: 389px; }
  .contact-icon { position: absolute; width: 34px; height: 34px; }
  .contact-icon--phone { left: 22px; top: 384px; }
  .contact-icon--email { left: 394px; top: 384px; }
  .assist-note {
    position: absolute; left: 0; width: 754px; top: 428px; text-align: center;
    font-family: "Lexend", sans-serif; font-size: 19.5px; line-height: 1; color: var(--white);
  }
</style>
</head>
<body>

  <div class="side-label side-label--front">Front</div>
  <div class="side-label side-label--back">Back</div>

  <section class="card card--front" aria-label="Card front">
    <svg class="title-banner" viewBox="0 0 754 120" aria-hidden="true">
      <defs>
        <linearGradient id="bannerBlue" x1="0" y1="0" x2="1" y2="0">
          <stop offset="0" stop-color="#1c5aa8"/>
          <stop offset="1" stop-color="#1e88d0"/>
        </linearGradient>
        <linearGradient id="bannerGreen" x1="0" y1="0" x2="1" y2="0">
          <stop offset="0" stop-color="#4cae3f"/>
          <stop offset="1" stop-color="#8dc63f"/>
        </linearGradient>
      </defs>
      <polygon points="34,100 76,33 354,33 310,100" fill="url(#bannerBlue)"/>
      <polygon points="307,106 354,26 719,26 672,106" fill="url(#bannerGreen)"/>
    </svg>
    <div class="title-word title-word--water">WATER</div>
    <div class="title-word title-word--atm"><strong>ATM</strong> <span>CARD</span></div>

    <div class="brand-name">CEDAR BROOK</div>
    <div class="brand-tagline">Purified Spring Water</div>

    <div class="water-photo" role="img" aria-label="Close-up photograph of splashing clear blue water with bubbles"></div>

    <svg class="front-wave" viewBox="0 0 754 59" preserveAspectRatio="none" aria-hidden="true">
      <path d="M0,14 C30,16 55,38 110,38 C170,38 220,24 280,30 C320,34 330,8 370,10 C410,12 420,36 470,38 C530,40 580,34 620,36 C680,38 700,20 754,10 L754,59 L0,59 Z" fill="var(--navy)"/>
      <path d="M0,14 C30,16 55,38 110,38 C170,38 220,24 280,30 C320,34 330,8 370,10 C410,12 420,36 470,38 C530,40 580,34 620,36 C680,38 700,20 754,10" fill="none" stroke="var(--white)" stroke-width="3"/>
    </svg>

    <div class="price-badge">
      <span class="price-label">PRICE</span>
      <span class="price-value">$100</span>
    </div>
  </section>

  <section class="card card--back" aria-label="Card back">
    <div class="back-top-band"></div>
    <div class="back-stripe"></div>
    <div class="back-panel"></div>
    <div class="chip"></div>
    <p class="usage-note">Lorem ipsum dolor sit amet, consectetuer adipiscing elit, sed diam nonummy nibh euismod tincidunt ut laoreet dolore magna aliquam erat volutpat.</p>

    <svg class="back-wave" viewBox="0 0 754 184" preserveAspectRatio="none" aria-hidden="true">
      <path d="M0,6 C40,8 70,34 120,34 C180,34 230,26 280,30 C330,34 350,6 390,6 C430,6 450,32 500,34 C560,36 600,32 640,34 C690,36 710,10 754,6 L754,184 L0,184 Z" fill="var(--navy)"/>
      <path d="M0,6 C40,8 70,34 120,34 C180,34 230,26 280,30 C330,34 350,6 390,6 C430,6 450,32 500,34 C560,36 600,32 640,34 C690,36 710,10 754,6" fill="none" stroke="var(--white)" stroke-width="3.5"/>
    </svg>

    <h2 class="contact-heading">PLEASE CONTACT</h2>

    <svg class="contact-icon contact-icon--phone" viewBox="0 0 34 34" aria-hidden="true">
      <rect x="6" y="6" width="22" height="22" transform="rotate(45 17 17)" fill="var(--green-light)"/>
      <path d="M12.5,11.5 l2.5,-1 l1.8,3.2 l-1.5,1.2 c0.8,1.8 2,3 3.8,3.8 l1.2,-1.5 l3.2,1.8 l-1,2.5 c-5,0.5 -10.5,-5 -10,-10 z" fill="var(--white)"/>
    </svg>
    <div class="contact-line contact-line--phone">(869) 614 2938, (869) 731 4072</div>

    <svg class="contact-icon contact-icon--email" viewBox="0 0 34 34" aria-hidden="true">
      <rect x="6" y="6" width="22" height="22" transform="rotate(45 17 17)" fill="var(--green-light)"/>
      <rect x="10.5" y="12.5" width="13" height="9" fill="var(--white)"/>
      <path d="M10.5,12.5 L17,17.5 L23.5,12.5" fill="none" stroke="var(--green-light)" stroke-width="1.2"/>
    </svg>
    <div class="contact-line contact-line--email">clearflowhq@examplemail.com</div>

    <p class="assist-note">For any Assistance or Recharging of Card</p>
  </section>

</body>
</html>
```